Web Design job: SaaS start-up needs a cutting-edge web design

What's Needed:
- All designs files created
- Fully coded implementation in HTML/CSS/Bootstrap
- Pages: 5 -- see content here http://www.TeamVellora.com
-- Home Page
-- The Hidden Value
-- Benefits
-- About us
-- Careers
- The existing site has the textual content for each page. We can tweak to meet specific designs if needed.
- You will need to update/create image and interactive content for pages.

Reference:
Our existing website has a lot of content on it for reference -
http://www.TeamVellora.com

Description:
We need a web design that focuses in the UX and conveys the idea of magically fixing company problems by way of using our software.

Home Page
The main goal is to Drive Sales of the SaaS tool. When a visitor lands on our home page they should see: What we do, How we can help their problem and How to contact us.
1. Quickly understand What We Do
-- we sell SaaS software.
-- Need to quickly convey what our software does. It's seems complicated but really its not. See the description in about us for more info and visit our existing site.

2. How we can help their problem
-- We aim to solve any problem related to employees
-- Even if the visitor does not have a specific problem in mind, there are several areas organizations can always improve: (some examples below)
---- Create Stronger, More Productive Teams
---- Build Better Communications Pathways
---- Encourage Innovation and Positive Change
---- Develop and Retain Strong "Company Culture"

3. Be able to Contact Us to get started
-- contacting us to get a sales lead is the ultimate goal.
-- the user should not have to hunt to contact us. needs to be easy.

Other Pages (Hidden Value, Benefit, About Us, Careers):
-- These are informative pages about our software and process.
-- If we grab the attention of the user on the home page then these are the pages that they will explore for more info.
-- Should be able to link to these pages from the main nav or from sections with the homepage. For example: What We Do sections could link to the benefits page. How we help their problem sections could link to the Hidden Value page. Regardless of what links to where, the idea is that we will be able to nav to other areas.

About Us:
Our company name is TeamVellora (as in Organizational Analysis). We provide a software as a service (SaaS) that uses a simple 6-question survey to analyze the relationships of people within an Organization and provide leaders with ground-breaking Insights about their teams, interactive social network data visualizations to explore their team's composition and we give detailed profiles of the key players (i.e, who are the Social Bridges, Who are the Knowledge Bottlenecks, Who are the Best Mentors, Who are the people that are completely disconnected/out of the loop). Leaders then use this information to make high level organizational decisions.

What's unique about our software:
-- Powerful analysis results from just a 6-question "pulse-surveys"
-- Innovative Tools for visually exploring the organization through relationships as opposed to org-chart
-- Get real-time results as opposed to waiting months with traditional methods
-- Traditional Org-charts represent the organization's skeleton, whereas we uncover the organization's neural network (how it solves problems).

Preferred fonts (but could be convinced otherwise if looks great):
-- Section titles - Aleo
-- Main body - Lato
-- TeamVellora logo - Philosopher

Things we like:
-- We like a big slider as the top of the landing page.

Colors to include:
-- Colors in the logo (red, blue, green, teal) as accent colors

Feel of the site:
-- Cutting-edge Software
-- Professional
-- Social Network flare (we analyze relationships)

Note:
If we find a great match with a designer there is strong possibility to continue the relationship with follow on work redesigning our web-based application.

Target Market(s)

Current customers are Corwin Pale & Hargrove, Upland Mutual Bank.
We target anyone that manages a large team. Such as Corporate Leaders, High Level Managers, HR Leaders

Industry/Entity Type

Business Software

Contact Information for Business Card

Logo image
Name of company "TEAMVELLORA" In Philosopher font.
Tagline: "Unlock the Hidden Value In Your Teams"
Person's Name, Title, email, phone.

Coding

Coded - Design and coding required

Number of Pages Required

4 page

Font styles to use
Other font styles liked:
• Lato, Philosopher, Aero

Colors
ec1f27
0255a3

Requirements
Must have
• See description.
Nice to have
• Things we like:
• We like a big slider as the top of the landing page. Ours is a little clunky and outdated but something fresh and sleek would be great.
• Colors to include:
• We would like to use the colors in the logo as accent colors in the site to give a consistent look and feel.
• Feel of the site:
• Cutting-edge Software
• Professional
• Social Network flare (we analyze relationships)

```html
<!DOCTYPE html>
<html lang="en">
<head>
<meta charset="utf-8">
<title>TeamVellora – Home</title>
<link href="https://fonts.googleapis.com/css2?family=Aleo:wght@400;700&family=Lato:wght@400;700&display=swap" rel="stylesheet">
<style>
:root{
  --red:#ec1f27;
  --blue:#0255a3;
  --link-blue:#1a7bbf;
  --ink:#333;
  --body:#555;
  --muted:#888;
  --band:#ececec;
  --footer:#e6e6e6;
  --line:#d6d6d6;
  --white:#fff;
}
*{box-sizing:border-box;margin:0;padding:0}
html,body{width:1200px;height:3120px;overflow:hidden}
body{font-family:'Lato',sans-serif;color:var(--ink);background:var(--white);position:relative}
.section{position:absolute;left:0;width:1200px;overflow:hidden}
.btn-outline{position:absolute;display:flex;align-items:center;justify-content:center;border:2px solid var(--red);color:var(--red);font:700 12px 'Lato',sans-serif;letter-spacing:1px;background:var(--white)}

/* header */
.site-header{top:0;height:110px;background:var(--white);box-shadow:0 1px 4px rgba(0,0,0,.08);z-index:2}
.brand{position:absolute;left:115px;top:34px;display:flex;align-items:center;gap:12px}
.brand-dot{width:40px;height:40px;border-radius:50%;background:var(--blue)}
.brand-name{font:700 25px 'Lato',sans-serif;color:var(--blue);letter-spacing:1px}
.main-nav a{position:absolute;top:36px;height:38px;display:flex;align-items:center;font:400 14px 'Lato',sans-serif;color:#777;text-decoration:none;white-space:nowrap}
.main-nav a.active{left:458px;width:88px;justify-content:center;border:2px solid var(--blue);color:var(--blue);font-weight:700;border-radius:3px}
.login{position:absolute;left:998px;top:34px;width:86px;height:38px;background:var(--red);color:var(--white);font:700 14px 'Lato',sans-serif;display:flex;align-items:center;justify-content:center;border-radius:2px}

/* hero */
.hero{top:110px;height:508px}
.hero-photo{position:absolute;inset:0;background:
  radial-gradient(circle at 4% 22%,rgba(70,150,60,.75) 0,rgba(70,150,60,0) 120px),
  radial-gradient(circle at 96% 82%,rgba(30,80,170,.8) 0,rgba(30,80,170,0) 130px),
  radial-gradient(circle at 52% 8%,rgba(200,205,210,.35) 0,rgba(200,205,210,0) 140px),
  radial-gradient(ellipse at 50% 50%,#44474a 0%,#2b2e30 60%,#1d1f20 100%)}
.hero-title{position:absolute;top:180px;width:100%;text-align:center;font:700 52px 'Aleo',serif;color:var(--white);text-shadow:0 2px 6px rgba(0,0,0,.5)}
.hero-sub{position:absolute;top:252px;width:100%;text-align:center;font:700 26px 'Aleo',serif;color:var(--white);letter-spacing:1px;text-shadow:0 2px 6px rgba(0,0,0,.5)}
.dots{position:absolute;top:468px;left:0;width:100%;display:flex;justify-content:center;gap:12px}
.dots span{width:13px;height:13px;border-radius:50%;background:rgba(255,255,255,.5)}
.dots span.on{background:var(--white)}

/* about */
.about{top:618px;height:453px;background:var(--white)}
.about-photo{position:absolute;left:624px;top:0;width:576px;height:453px;background:
  radial-gradient(ellipse at 70% 55%,#b7cbe0 0%,rgba(183,203,224,0) 55%),
  radial-gradient(circle at 58% 28%,#b98a6c 0,rgba(185,138,108,0) 70px),
  linear-gradient(90deg,#fff 0%,#eef0f2 35%,#dfe4e9 100%)}
.about h2{position:absolute;left:125px;top:88px;font:400 32px 'Aleo',serif;color:var(--ink)}
.about p{position:absolute;left:125px;top:143px;width:610px;font:400 14px/29px 'Lato',sans-serif;color:var(--body)}

/* what we do */
.what{top:1071px;height:381px;background:var(--band)}
.what h2{position:absolute;top:40px;width:100%;text-align:center;font:400 30px 'Aleo',serif;color:var(--ink)}
.feature{position:absolute;top:104px;width:230px;text-align:center}
.feature .icon{width:118px;height:118px;margin:0 auto;border-radius:50%;background:var(--red);border:5px solid var(--white);box-shadow:0 2px 6px rgba(0,0,0,.2);display:flex;align-items:center;justify-content:center}
.feature h3{margin-top:20px;font:400 18px/22px 'Aleo',serif;color:var(--link-blue)}
.feature p{margin-top:10px;font:400 12.5px/19px 'Lato',sans-serif;color:var(--muted);padding:0 8px}

/* help */
.help{top:1452px;height:432px;background:radial-gradient(ellipse at 75% 40%,#0c63b6 0%,var(--blue) 55%,#014a8f 100%)}
.device{position:absolute;left:115px;top:80px;width:467px;height:240px}
.help h2{position:absolute;left:603px;top:56px;font:400 30px 'Aleo',serif;color:var(--white)}
.help .lead{position:absolute;left:606px;top:102px;width:480px;font:400 15px/23px 'Lato',sans-serif;color:var(--white)}
.help ul{position:absolute;left:606px;top:190px;list-style:none}
.help li{font:400 13.5px/32px 'Lato',sans-serif;color:var(--white)}
.help li::before{content:"›";font-weight:700;margin-right:12px}
.btn-ghost{position:absolute;left:610px;top:331px;width:125px;height:38px;border:2px solid var(--white);color:var(--white);font:700 13px 'Lato',sans-serif;display:flex;align-items:center;justify-content:center;letter-spacing:.5px}

/* solution */
.solution{top:1884px;height:437px;background:var(--white)}
.solution h2{position:absolute;left:141px;top:58px;font:400 30px 'Aleo',serif;color:var(--ink)}
.solution ul{position:absolute;left:145px;top:106px;width:510px;list-style:none}
.solution li{font:400 14px/30px 'Lato',sans-serif;color:var(--body)}
.tablet{position:absolute;left:709px;top:50px;width:288px;height:420px;border:2px solid var(--line);border-radius:28px;background:#f7f7f7}
.tablet-screen{position:absolute;left:12px;top:40px;width:260px;height:390px;background:
  radial-gradient(circle at 30% 12%,#e7c0a4 0,rgba(231,192,164,0) 60px),
  radial-gradient(ellipse at 55% 55%,#e4e4e4 0,rgba(228,228,228,0) 110px),
  linear-gradient(180deg,#ffffff 0%,#f3f3f3 100%)}

/* contact */
.contact{top:2321px;height:410px;background:var(--band);border-top:1px solid var(--line)}
.contact h2{position:absolute;top:36px;width:100%;text-align:center;font:400 30px 'Aleo',serif;color:var(--blue)}
.field{position:absolute;background:var(--white);border:1px solid var(--line);font:400 14px 'Lato',sans-serif;color:#999;padding:12px 14px}
.submit{position:absolute;left:526px;top:320px;width:154px;height:40px;background:var(--blue);color:var(--white);font:700 15px 'Lato',sans-serif;display:flex;align-items:center;justify-content:center;border-radius:2px}

/* offices */
.offices{top:2731px;height:223px;background:var(--white);border-top:1px solid var(--line)}
.office{position:absolute;top:54px;width:240px}
.office h4{font:700 15px 'Lato',sans-serif;color:var(--red);margin-bottom:18px}
.office .row{display:flex;align-items:center;gap:10px;font:400 14px 'Lato',sans-serif;color:var(--body);height:36px}
.office .row svg{flex:none}

/* footer */
.site-footer{top:2954px;height:166px;background:var(--footer)}
.foot-nav{position:absolute;top:40px;width:100%;display:flex;justify-content:center;gap:34px}
.foot-nav a{font:400 15px 'Lato',sans-serif;color:var(--ink);text-decoration:none}
.copyright{position:absolute;top:74px;width:100%;text-align:center;font:400 13px 'Lato',sans-serif;color:#999}
.social{position:absolute;top:108px;width:100%;display:flex;justify-content:center;gap:12px}
.social span{width:36px;height:36px;border-radius:50%;background:var(--blue)}
</style>
</head>
<body>

<header class="section site-header">
  <div class="brand"><span class="brand-dot"></span><span class="brand-name">TEAMVELLORA</span></div>
  <nav class="main-nav">
    <a class="active" href="#">HOME</a>
    <a href="#" style="left:568px">ABOUT US</a>
    <a href="#" style="left:676px">BENEFITS</a>
    <a href="#" style="left:778px">CAREER</a>
    <a href="#" style="left:871px">HIDDEN VALUE</a>
  </nav>
  <div class="login">LOGIN</div>
</header>

<section class="section hero">
  <div class="hero-photo" role="img" aria-label="Team members around a chalkboard table sketched with a SaaS box"></div>
  <h1 class="hero-title">THE EXPERIENCED ECONOMY</h1>
  <p class="hero-sub">SHARED LEARNING &amp; OPPORTUNITIES</p>
  <div class="dots"><span></span><span class="on"></span><span></span><span></span></div>
</section>

<section class="section about">
  <div class="about-photo" role="img" aria-label="Man celebrating at his laptop"></div>
  <h2>ABOUT TEAMVELLORA</h2>
  <p>Our company name is TeamVellora (as in Organizational Analysis). We provide a software as a service (SaaS) that uses a simple 6-question survey to analyze the relationships of people within an Organization and provide leaders with ground-breaking Insights about their teams, interactive social network data visualizations to explore their team's composition and we give detailed profiles of the key players</p>
  <div class="btn-outline" style="left:125px;top:310px;width:125px;height:36px">READ MORE</div>
</section>

<section class="section what">
  <h2>WHAT WE DO</h2>
  <div class="feature" style="left:120px">
    <div class="icon"><svg width="48" height="44" viewBox="0 0 48 44" fill="none" stroke="#fff" stroke-width="3"><rect x="3" y="3" width="42" height="28" rx="2"/><path d="M18 40h12M24 31v9"/></svg></div>
    <h3>Online Pulse<br>Survey</h3>
    <p>Morbi diam mauris viverra in gravida eu mattis in arte Morbi</p>
  </div>
  <div class="feature" style="left:365px">
    <div class="icon"><svg width="48" height="46" viewBox="0 0 48 46" fill="none" stroke="#fff" stroke-width="3"><circle cx="24" cy="7" r="5"/><circle cx="8" cy="38" r="5"/><circle cx="24" cy="38" r="5"/><circle cx="40" cy="38" r="5"/><path d="M24 12v9M8 33v-12h32v12M24 21v12"/></svg></div>
    <h3>Proprietary<br>Algorithms</h3>
    <p>Morbi diam mauris viverra in gravida eu mattis in arte Morbi</p>
  </div>
  <div class="feature" style="left:611px">
    <div class="icon"><svg width="48" height="48" viewBox="0 0 48 48" fill="none" stroke="#fff" stroke-width="3"><circle cx="32" cy="16" r="10"/><path d="M25 23L6 42M10 38l5 5M15 33l5 5"/></svg></div>
    <h3>Organizational<br>key Insights</h3>
    <p>Morbi diam mauris viverra in gravida eu mattis in arte Morbi</p>
  </div>
  <div class="feature" style="left:856px">
    <div class="icon"><svg width="50" height="44" viewBox="0 0 50 44" fill="none" stroke="#fff" stroke-width="3"><path d="M4 4h42v26H20l-9 9v-9H4z"/><circle cx="16" cy="17" r="1.5" fill="#fff"/><circle cx="25" cy="17" r="1.5" fill="#fff"/><circle cx="34" cy="17" r="1.5" fill="#fff"/></svg></div>
    <h3>Expert Review and<br>Action Plans</h3>
    <p>Morbi diam mauris viverra in gravida eu mattis in arte Morbi</p>
  </div>
</section>

<section class="section help">
  <svg class="device" viewBox="0 0 467 240">
    <defs>
      <radialGradient id="screenTone" cx="50%" cy="48%" r="60%">
        <stop offset="0" stop-color="#e9c6dc"/>
        <stop offset=".5" stop-color="#eef0fa"/>
        <stop offset="1" stop-color="#fafafa"/>
      </radialGradient>
    </defs>
    <rect x="0" y="40" width="70" height="150" rx="8" fill="#222"/>
    <rect x="60" y="0" width="360" height="225" rx="8" fill="#1c1c1c"/>
    <rect x="72" y="12" width="336" height="200" fill="url(#screenTone)" role="img" aria-label="Social network graph visualization"/>
    <rect x="40" y="225" width="420" height="12" rx="5" fill="#cfd3d6"/>
  </svg>
  <h2>How we can help their problem</h2>
  <p class="lead">We aim to solve any problem related to employees<br>Even if the visitor does not have a specific problem in mind, there are several areas organizations can always improve:</p>
  <ul>
    <li>Create Stronger, More Productive Teams</li>
    <li>Build Better Communications Pathways</li>
    <li>Encourage Innovation and Positive Change</li>
    <li>Develop and Retain Strong "Company Culture"</li>
  </ul>
  <div class="btn-ghost">READ MORE</div>
</section>

<section class="section solution">
  <h2>OUR SOLUTION</h2>
  <ul>
    <li>FIRST Data-Driven Platform with Innovative Tools for Dynamic, Real-Time Analyses and Exploration of Employee Relationships</li>
    <li>Powerful analysis results from just a 6-question "pulse-surveys"</li>
    <li>Innovative Tools for visually exploring the organization through relationships as opposed to org-chart</li>
    <li>Get real-time results as opposed to waiting months with traditional methods</li>
  </ul>
  <div class="btn-outline" style="left:145px;top:328px;width:126px;height:36px">READ MORE</div>
  <div class="tablet"><div class="tablet-screen" role="img" aria-label="Hand touching a sketched SaaS cloud linked to devices"></div></div>
</section>

<section class="section contact">
  <h2>CONTACT US</h2>
  <div class="field" style="left:185px;top:92px;width:412px;height:41px">Your Name</div>
  <div class="field" style="left:605px;top:92px;width:414px;height:41px">Email address</div>
  <div class="field" style="left:185px;top:142px;width:412px;height:41px">Phone</div>
  <div class="field" style="left:605px;top:142px;width:414px;height:41px">Location</div>
  <div class="field" style="left:185px;top:196px;width:834px;height:100px">Message</div>
  <div class="submit">GET STARTED</div>
</section>

<section class="section offices">
  <div class="office" style="left:116px">
    <h4>CINCINNATI, OH</h4>
    <div class="row"><svg width="28" height="28" viewBox="0 0 28 28"><circle cx="14" cy="14" r="13" fill="none" stroke="#0255a3" stroke-width="2"/><path d="M10 8l3 3-2 2c1 2 2 3 4 4l2-2 3 3-2 2c-5 0-10-5-10-10z" fill="#0255a3"/></svg>(555)-938-0171</div>
    <div class="row"><svg width="28" height="28" viewBox="0 0 28 28"><circle cx="14" cy="14" r="13" fill="none" stroke="#0255a3" stroke-width="2"/><rect x="8" y="10" width="12" height="9" fill="#0255a3"/><path d="M8 10l6 5 6-5" stroke="#fff" fill="none"/></svg>cincinnati@teamvellora.com</div>
  </div>
  <div class="office" style="left:368px">
    <h4>DENVER, CO</h4>
    <div class="row"><svg width="28" height="28" viewBox="0 0 28 28"><circle cx="14" cy="14" r="13" fill="none" stroke="#0255a3" stroke-width="2"/><path d="M10 8l3 3-2 2c1 2 2 3 4 4l2-2 3 3-2 2c-5 0-10-5-10-10z" fill="#0255a3"/></svg>(555)-964-0150</div>
    <div class="row"><svg width="28" height="28" viewBox="0 0 28 28"><circle cx="14" cy="14" r="13" fill="none" stroke="#0255a3" stroke-width="2"/><rect x="8" y="10" width="12" height="9" fill="#0255a3"/><path d="M8 10l6 5 6-5" stroke="#fff" fill="none"/></svg>denver@teamvellora.com</div>
  </div>
  <div class="office" style="left:620px">
    <h4>BIRMINGHAM, AL</h4>
    <div class="row"><svg width="28" height="28" viewBox="0 0 28 28"><circle cx="14" cy="14" r="13" fill="none" stroke="#0255a3" stroke-width="2"/><path d="M10 8l3 3-2 2c1 2 2 3 4 4l2-2 3 3-2 2c-5 0-10-5-10-10z" fill="#0255a3"/></svg>(555)-704-0110</div>
    <div class="row"><svg width="28" height="28" viewBox="0 0 28 28"><circle cx="14" cy="14" r="13" fill="none" stroke="#0255a3" stroke-width="2"/><rect x="8" y="10" width="12" height="9" fill="#0255a3"/><path d="M8 10l6 5 6-5" stroke="#fff" fill="none"/></svg>birmingham@teamvellora.com</div>
  </div>
  <div class="office" style="left:871px">
    <h4>CHICAGO, IL</h4>
    <div class="row"><svg width="28" height="28" viewBox="0 0 28 28"><circle cx="14" cy="14" r="13" fill="none" stroke="#0255a3" stroke-width="2"/><path d="M10 8l3 3-2 2c1 2 2 3 4 4l2-2 3 3-2 2c-5 0-10-5-10-10z" fill="#0255a3"/></svg>(555)-964-0150</div>
    <div class="row"><svg width="28" height="28" viewBox="0 0 28 28"><circle cx="14" cy="14" r="13" fill="none" stroke="#0255a3" stroke-width="2"/><rect x="8" y="10" width="12" height="9" fill="#0255a3"/><path d="M8 10l6 5 6-5" stroke="#fff" fill="none"/></svg>chicago@teamvellora.com</div>
  </div>
</section>

<footer class="section site-footer">
  <nav class="foot-nav">
    <a href="#">HOME</a><a href="#">ABOUT US</a><a href="#">BENEFITS</a><a href="#">CAREER</a><a href="#">HIDDEN VALUE</a>
  </nav>
  <p class="copyright">© 2016 Company Name  All right reserved</p>
  <div class="social" aria-label="Social links"><span></span><span></span><span></span><span></span></div>
</footer>

</body>
</html>
```